BrightKestrel - IT Consultancy Website

Our company is called BrightKestrel and our purpose is to help companies sustainably embrace and reap the benefits of cloud platforms, through transforming practices, skills and technology using DevOps and Security practices such that they are able to automate, manage and secure their cloud platforms to deliver product to market with increasing velocity.

To get our business started I require a website that will model the typical layout of an IT consultancy services company to an Australian Market. There are many examples of such a site, here are some of them. We would like a landing page and then a few simple menu options (About, Blog, Services etc..) to additional content

http://morvane.com.au/
http://www.pellixa.com.au/
http://www.tarno.com.au/

I require the site to be created with a separate CSS file that maintains the colour palette. This is a very important requirement, I want to be able to change the colours employed in the site in a single location and not have to scan through multiple files to replace the codes.

The website must be built using static content as it will not be hosted on a web server but instead in NBX using V7 and Pathwave CDN. Therefore please stick to HTML, JavaScript, CSS and other static file formats. The website needs to be response, smooth and reactive. It should render on desktop, mobile and tablet and feature smooth scrolling, transitions and fade in's.

The website should give the customer confidence that they are dealing with a highly professional IT services company, focused strongly on cloud (NBX, Kentrel Vista, Orvane Hub etc..), motivated by beautiful and fluid design.

In order to make this simpler for you, the designer, I have already purchased this template from https://quillframe.com/theme/northgate-versatile-layout-QX7K31904 and uploaded it. Feel free to use this template if you choose (note that it makes use of a separate color palette which is a key requirement) or use one of your own choosing. If you do use this template ensure that it does not look too much like "another bootstrap site" therefore use the layout and widgets but make the site look fresh and original too.
Obviously you must delete all trace of the bootstrap package once the project has completed if you do use it

Target Market(s)

Corporate and medium enterprise businesses

Industry/Entity Type

Information Technology

Coding

Coded - Design and coding required

Number of Pages Required

4 page

Font styles to use
Sans Serif

Colors
abd036
33a6d7

Requirements
Must have
• The website should give the customer confidence that they are dealing with a highly professional IT services company, focused strongly on cloud (NBX, Kentrel Vista, Orvane Hub etc..), motivated by beautiful and fluid design. Our company name is BrightKestrel, the site needs to pay homage to the themes of fluidity and logic
• Along with About Us, Services and a Blog page could I also get social logo's included too
Nice to have
• The website must be built using static content as it will not be hosted on a web server but instead in NBX using V7 and Pathwave CDN. Therefore please stick to HTML, JavaScript, CSS and other static file formats. The website needs to be response, smooth and reactive. It should render on desktop, mobile and tablet and feature smooth scrolling, transitions and fade in's.
Should not have
• Lurid colours, or too much animations. The design must "flow"

```html
<!DOCTYPE html>
<html lang="en">
<head>
<meta charset="utf-8">
<title>BrightKestrel IT Consultancy</title>
<link href="https://fonts.googleapis.com/css2?family=Roboto:wght@300;400;500;700&display=swap" rel="stylesheet">
<style>
:root{
  --blue:#1ba6de;
  --blue-dark:#1590c2;
  --ink:#333;
  --text:#666;
  --muted:#888;
  --topbar:#3a3a3a;
  --band-dark:#222;
  --light:#f2f2f2;
  --footer:#f6f6f6;
  --white:#fff;
  --line:#dedede;
}
*{box-sizing:border-box;margin:0;padding:0}
html,body{width:1200px;height:3543px;overflow:hidden}
body{font-family:'Roboto',sans-serif;color:var(--text);background:var(--white);position:relative}
.section{position:absolute;left:0;width:1200px}
.center{text-align:center}
.section-title{font-size:26px;font-weight:400;color:var(--ink);text-align:center}
.section-title b{color:var(--blue);font-weight:500}
.intro{width:860px;margin:14px auto 0;font-size:12.5px;line-height:22px;text-align:center;color:var(--text)}
.btn-outline{display:flex;align-items:center;justify-content:center;gap:10px;border:2px solid var(--white);color:var(--white);font-size:14px;font-weight:500;letter-spacing:.5px;border-radius:3px}

/* top bar */
.topbar{top:0;height:57px;background:var(--topbar);display:flex;align-items:center;justify-content:space-between;padding:0 99px;color:#ddd;font-size:13px}
.social{display:flex;gap:8px}
.social span{width:20px;height:20px;border:1.5px solid #ccc;border-radius:50%}
.contact{display:flex;gap:34px}
.contact span{display:flex;align-items:center;gap:7px}

/* header */
.header{top:57px;height:85px;display:flex;align-items:center;justify-content:space-between;padding:0 99px;box-shadow:0 2px 4px rgba(0,0,0,.06)}
.logo{font-size:24px;font-weight:500;color:var(--ink);letter-spacing:-.5px}
.nav{display:flex;align-items:center;gap:44px;font-size:13px;font-weight:500;color:#444}
.nav .active{color:var(--blue)}
.search{width:38px;height:38px;border:2px solid var(--blue);border-radius:50%;display:flex;align-items:center;justify-content:center}

/* hero */
.hero{top:142px;height:574px;background:linear-gradient(160deg,#2f3e4a 0%,#1b2630 50%,#26323c 100%)}
.hero-title{position:absolute;top:535px;left:0;width:100%;text-align:center;font-size:50px;font-weight:400;color:var(--blue);top:393px}
.hero-text{position:absolute;top:462px;left:0;width:100%;text-align:center;font-size:13px;line-height:24px;color:#eee}
.arrow{position:absolute;top:268px;width:38px;height:38px;border:2px solid #ddd;border-radius:50%;display:flex;align-items:center;justify-content:center}

/* features */
.features{top:716px;height:529px;padding-top:30px}
.cards{position:absolute;top:148px;left:99px;display:flex;gap:22px}
.card{width:320px;height:317px;border:1px solid var(--line);box-shadow:0 8px 10px -6px rgba(0,0,0,.18);text-align:center;padding-top:17px}
.icon-circle{width:92px;height:92px;border-radius:50%;background:var(--blue);margin:0 auto;display:flex;align-items:center;justify-content:center}
.card h3{font-size:20px;font-weight:400;color:var(--ink);margin-top:34px}
.card p{font-size:12px;line-height:19px;width:260px;margin:18px auto 0}
.read{display:block;margin-top:22px;font-size:13px;font-weight:500;color:var(--blue)}

/* offer band */
.offer{top:1245px;height:149px;background:var(--blue);color:var(--white)}
.offer h2{position:absolute;left:99px;top:34px;font-size:23px;font-weight:500}
.offer p{position:absolute;left:99px;top:68px;width:720px;font-size:12px;line-height:20px}
.offer .btn-outline{position:absolute;left:917px;top:47px;width:184px;height:52px}

/* why */
.why{top:1394px;height:531px;padding-top:30px}
.monitor{position:absolute;left:99px;top:128px;width:373px;height:348px;background:linear-gradient(180deg,#3a4550 0%,#9fb2c0 70%,#e6e9ec 100%);border-radius:6px}
.why-copy{position:absolute;left:529px;top:142px;width:605px;font-size:12.5px;line-height:22px;text-align:justify}
.why-item{position:absolute;left:529px;display:flex;gap:20px;align-items:flex-start}
.why-item .dot{width:44px;height:44px;border-radius:50%;background:var(--blue);display:flex;align-items:center;justify-content:center;flex:none}
.why-item h4{font-size:15px;font-weight:500;color:var(--blue);margin-top:2px}
.why-item p{font-size:11.5px;margin-top:6px}
.btn-line{position:absolute;left:529px;top:436px;width:128px;height:44px;border:2px solid var(--line);color:var(--blue);font-size:12px;font-weight:500;display:flex;align-items:center;justify-content:center;gap:8px;border-radius:3px}

/* portfolio */
.portfolio{top:1925px;height:496px;background:var(--light);padding-top:32px}
.projects{position:absolute;top:154px;left:99px;display:flex;gap:7px}
.project{width:246px;height:290px;background:var(--white);border:1px solid var(--line);text-align:center}
.project .shot{height:177px}
.project h4{font-size:15px;font-weight:500;color:var(--ink);margin-top:20px}
.project p{font-size:11.5px;line-height:18px;width:210px;margin:8px auto 0}
.chev{position:absolute;top:210px}

/* testimonials */
.testimonials{top:2421px;height:383px;padding-top:40px}
.avatar{position:absolute;left:552px;top:103px;width:96px;height:96px;border-radius:50%;background:linear-gradient(180deg,#c9b19a,#8e7361);border:4px solid var(--white);box-shadow:0 2px 6px rgba(0,0,0,.25)}
.quote{position:absolute;top:230px;left:230px;width:740px;text-align:center;font-size:12.5px;line-height:22px}
.author{position:absolute;top:288px;left:0;width:100%;display:flex;justify-content:center;align-items:center;gap:18px;font-size:17px;color:var(--ink)}
.author i{width:60px;height:2px;background:var(--blue)}
.dots{position:absolute;top:330px;left:0;width:100%;display:flex;justify-content:center;gap:9px}
.dots span{width:14px;height:4px;background:#ccc}
.dots .on{background:var(--blue)}

/* stats */
.stats{top:2804px;height:278px;background:linear-gradient(180deg,#4b4f53,#6d7175 60%,#55595d)}
.stat{position:absolute;top:24px;width:200px;text-align:center;color:var(--white)}
.stat .ring{width:150px;height:150px;border:2px solid rgba(255,255,255,.8);border-radius:50%;margin:0 auto;display:flex;align-items:center;justify-content:center}
.stat .ring span{width:118px;height:118px;border-radius:50%;background:rgba(255,255,255,.2);display:flex;align-items:center;justify-content:center}
.stat h5{font-size:17px;font-weight:500;margin-top:20px}
.stat div.num{font-size:15px;margin-top:8px}

.cta{top:3082px;height:102px;background:var(--band-dark);color:var(--white)}
.cta h2{position:absolute;left:135px;top:36px;font-size:23px;font-weight:500}
.cta .btn-outline{position:absolute;left:917px;top:25px;width:184px;height:52px}

/* footer */
.footer{top:3184px;height:359px;background:var(--footer)}
.col{position:absolute;top:68px;font-size:12px;color:var(--text)}
.col h6{font-size:15px;font-weight:500;color:var(--ink);margin-bottom:22px;letter-spacing:.3px}
.col li{list-style:none;line-height:24px}
.news h6{margin-top:22px;margin-bottom:6px}
.email{width:226px;height:38px;background:var(--white);border:1px solid var(--line);margin-top:10px;font-size:11px;color:#aaa;padding:8px}
.subscribe{margin-top:12px;width:98px;height:36px;background:var(--blue);color:var(--white);font-size:12px;font-weight:500;display:flex;align-items:center;justify-content:center}
.follow li{display:flex;align-items:center;gap:16px;line-height:30px}
.follow li i{width:10px;height:10px;background:#555}
.copyright{position:absolute;left:99px;top:322px;font-size:11px;color:var(--ink)}
</style>
</head>
<body>

<div class="section topbar">
  <div class="social"><span></span><span></span><span></span><span></span><span></span></div>
  <div class="contact">
    <span><svg width="14" height="10" viewBox="0 0 14 10"><rect x=".5" y=".5" width="13" height="9" fill="none" stroke="#ddd"/><path d="M.5 .5 7 5.5 13.5 .5" fill="none" stroke="#ddd"/></svg>Email : info@brightkestrel.com</span>
    <span><svg width="12" height="12" viewBox="0 0 12 12"><path d="M2 1h3l1 3-2 1a7 7 0 0 0 3 3l1-2 3 1v3c-5 0-9-4-9-9z" fill="#ddd"/></svg>Call Us : (01)-555-0142</span>
  </div>
</div>

<header class="section header">
  <div class="logo">BrightKestrel <span style="color:var(--ink)">IT Consultancy</span></div>
  <nav class="nav">
    <span class="active">HOME</span><span>ABOUT</span><span>SKILLS</span><span>RECENT PROJECTS</span><span>CONTACT</span>
    <span class="search"><svg width="16" height="16" viewBox="0 0 16 16"><circle cx="7" cy="7" r="5" fill="none" stroke="#1ba6de" stroke-width="2"/><path d="M11 11l4 4" stroke="#1ba6de" stroke-width="2"/></svg></span>
  </nav>
</header>

<section class="section hero" role="img" aria-label="Team of consultants working together at a desk with laptops and documents">
  <div class="arrow" style="left:60px"><svg width="12" height="14" viewBox="0 0 12 14"><path d="M9 1 3 7l6 6" fill="none" stroke="#ddd" stroke-width="2"/></svg></div>
  <div class="arrow" style="left:1102px"><svg width="12" height="14" viewBox="0 0 12 14"><path d="M3 1l6 6-6 6" fill="none" stroke="#ddd" stroke-width="2"/></svg></div>
  <h1 class="hero-title">IT SERVICES COMPANY</h1>
  <p class="hero-text">Praesentium voluptatum deleniti atque corrupti quos dolores et quas molestias excepturi sint occaecati cupiditate non provident,<br>similique sunt in culpa qui officia deserunt mollitia animi, id est laborum et dolorum fuga.</p>
</section>

<section class="section features">
  <h2 class="section-title">Our <b>Features</b></h2>
  <p class="intro">Beguiled and demoralized by the charms of pleasure of the moment, so blinded by desire, that they cannot foresee the pain and trouble that are bound to ensue; and equal blame belongs to those who fail in their duty through weakness of will, which is the same as saying through shrinking from toil and pain.</p>
  <div class="cards">
    <div class="card">
      <div class="icon-circle"><svg width="44" height="44" viewBox="0 0 44 44" fill="none" stroke="#fff" stroke-width="2.5"><circle cx="15" cy="14" r="6"/><path d="M5 34c0-7 4-11 10-11"/><rect x="20" y="20" width="18" height="12"/><path d="M17 36h24"/></svg></div>
      <h3>Consultancy</h3>
      <p>Praesentium voluptatum deleniti atque corrupti quos dolores et quas molestias excepturi sint occaecati cupiditate non provident, similique sunt</p>
      <span class="read">Read More ›</span>
    </div>
    <div class="card">
      <div class="icon-circle"><svg width="46" height="32" viewBox="0 0 46 32"><path d="M12 30a10 10 0 0 1-1-20 13 13 0 0 1 25 3 8 8 0 0 1 0 17z" fill="#fff"/></svg></div>
      <h3>Cloud Platforms</h3>
      <p>Praesentium voluptatum deleniti atque corrupti quos dolores et quas molestias excepturi sint occaecati cupiditate non provident, similique sunt</p>
      <span class="read">Read More ›</span>
    </div>
    <div class="card">
      <div class="icon-circle"><svg width="48" height="34" viewBox="0 0 48 34"><path d="M2 10l10-6 8 4 8-4 10 2 8 8-16 16-6-4-4 2-6-6-6-2-6-10z" fill="#fff"/></svg></div>
      <h3>Transforming Practices</h3>
      <p>Praesentium voluptatum deleniti atque corrupti quos dolores et quas molestias excepturi sint occaecati cupiditate non provident, similique sunt</p>
      <span class="read">Read More ›</span>
    </div>
  </div>
</section>

<section class="section offer">
  <h2>DON'T MISS OUT OUR OFFERS</h2>
  <p>Deleniti atque corrupti quos dolores et quas molestias excepturi sint occaecati cupiditate non provident, similique sunt in culpa deserunt mollitia animi, et est laborum et dolorum fuga. Et harum quidem rerum facilis est et expedita distinctio.</p>
  <div class="btn-outline">LEARN MORE <svg width="14" height="12" viewBox="0 0 14 12"><path d="M0 6h11M7 1l5 5-5 5" fill="none" stroke="#fff" stroke-width="2.5"/></svg></div>
</section>

<section class="section why">
  <h2 class="section-title">Why <b>Choose</b> Us</h2>
  <p class="intro">Beguiled and demoralized by the charms of pleasure of the moment, so blinded by desire, that they cannot foresee the pain and trouble that are bound to ensue; and equal blame belongs to those who fail in their duty through weakness of will, which is the same as saying through shrinking from toil and pain.</p>
  <div class="monitor" role="img" aria-label="Desktop computer showing the website homepage, with keyboard and mouse"></div>
  <p class="why-copy">Deleniti atque corrupti quos dolores et quas molestias excepturi sint occaecati cupiditate non provident, similique sunt in culpa qui officia deserunt mollitia animi, id est laborum et dolorum</p>
  <div class="why-item" style="top:204px"><span class="dot"><svg width="22" height="16" viewBox="0 0 22 16"><path d="M1 5l5-3 4 2 4-2 5 1 2 4-8 8-3-2-3 1-3-3z" fill="#fff"/></svg></span><div><h4>Deleniti atque corrupti</h4><p>Cupiditate non provident, similique sunt in culpa qui officia deserunt mollitia</p></div></div>
  <div class="why-item" style="top:280px"><span class="dot"><svg width="20" height="18" viewBox="0 0 20 18"><path d="M2 6h4l9-5v16l-9-5H2z" fill="#fff"/></svg></span><div><h4>Deleniti atque corrupti</h4><p>Cupiditate non provident, similique sunt in culpa qui officia deserunt mollitia</p></div></div>
  <div class="why-item" style="top:356px"><span class="dot"><svg width="18" height="18" viewBox="0 0 18 18" fill="none" stroke="#fff" stroke-width="2"><rect x="2" y="2" width="14" height="14"/><path d="M5 7h8M5 11h5"/></svg></span><div><h4>Deleniti atque corrupti</h4><p>Cupiditate non provident, similique sunt in culpa qui officia deserunt mollitia</p></div></div>
  <div class="btn-line">LEARN MORE <svg width="12" height="10" viewBox="0 0 14 12"><path d="M0 6h11M7 1l5 5-5 5" fill="none" stroke="#1ba6de" stroke-width="2.5"/></svg></div>
</section>

<section class="section portfolio">
  <h2 class="section-title">Our <b>Portfolio</b></h2>
  <p class="intro">Beguiled and demoralized by the charms of pleasure of the moment, so blinded by desire, that they cannot foresee the pain and trouble that are bound to ensue; and equal blame belongs to those who fail in their duty through weakness of will, which is the same as saying through shrinking from toil and pain.</p>
  <svg class="chev" style="left:72px" width="18" height="100" viewBox="0 0 18 100"><path d="M16 2 2 50l14 48" fill="none" stroke="#bbb" stroke-width="2"/></svg>
  <svg class="chev" style="left:1110px" width="18" height="100" viewBox="0 0 18 100"><path d="M2 2l14 48L2 98" fill="none" stroke="#bbb" stroke-width="2"/></svg>
  <div class="projects">
    <div class="project"><div class="shot" role="img" aria-label="Hands holding a blue cloud" style="background:linear-gradient(180deg,#cfe3f3,#6fa9d6)"></div><h4>PROJECT TITLE</h4><p>Deserunt mollitia animi, id est laborum et dolorum fuga Et harum quidem rerum facilis est et expedita</p></div>
    <div class="project"><div class="shot" role="img" aria-label="Businessman holding a glowing globe" style="background:linear-gradient(180deg,#1d3450,#3c6f9c)"></div><h4>PROJECT TITLE</h4><p>Deserunt mollitia animi, id est laborum et dolorum fuga Et harum quidem rerum facilis est et expedita</p></div>
    <div class="project"><div class="shot" role="img" aria-label="Network of cloud icons on a blue screen" style="background:linear-gradient(180deg,#0c2a4a,#1f6aa8)"></div><h4>PROJECT TITLE</h4><p>Deserunt mollitia animi, id est laborum et dolorum fuga Et harum quidem rerum facilis est et expedita</p></div>
    <div class="project"><div class="shot" role="img" aria-label="Hands using a tablet with a cloud above" style="background:linear-gradient(180deg,#1a1d20,#5d6267)"></div><h4>PROJECT TITLE</h4><p>Deserunt mollitia animi, id est laborum et dolorum fuga Et harum quidem rerum facilis est et expedita</p></div>
  </div>
</section>

<section class="section testimonials">
  <h2 class="section-title">Our <b>Testimonials</b></h2>
  <div class="avatar" role="img" aria-label="Portrait photo of the client"></div>
  <p class="quote">We are so grateful we chose Wordwise Speech Studio to teach our daughter, her speech has improved immensely in 5 months.... you have been a terrific teacher, who is very kind and caring, thankyou so much!" (Mother of Nerys)</p>
  <div class="author"><i></i>Darren Vale<i></i></div>
  <div class="dots"><span></span><span class="on"></span><span></span><span></span></div>
</section>

<section class="section stats" role="img" aria-label="Dimmed office background photo behind counters">
  <div class="stat" style="left:124px"><div class="ring"><span><svg width="44" height="40" viewBox="0 0 44 40" fill="none" stroke="#fff" stroke-width="2.5"><rect x="2" y="4" width="30" height="22"/><path d="M10 34h14M17 26v8"/><circle cx="34" cy="12" r="7"/></svg></span></div><h5>PROJECTS</h5><div class="num">1525</div></div>
  <div class="stat" style="left:380px"><div class="ring"><span><svg width="44" height="32" viewBox="0 0 44 32" fill="#fff"><circle cx="22" cy="8" r="6"/><circle cx="9" cy="11" r="4"/><circle cx="35" cy="11" r="4"/><path d="M12 30c0-9 4-14 10-14s10 5 10 14zM2 28c0-7 3-10 7-10 2 0 3 1 4 2-2 3-2 5-2 8zM42 28c0-7-3-10-7-10-2 0-3 1-4 2 2 3 2 5 2 8z"/></svg></span></div><h5>CLIENTS</h5><div class="num">258</div></div>
  <div class="stat" style="left:639px"><div class="ring"><span><svg width="40" height="38" viewBox="0 0 40 38" fill="#fff"><path d="M16 2h8v14h7L20 28 9 16h7z"/><path d="M2 24h8l6 6h8l6-6h8v12H2z"/></svg></span></div><h5>DOWNLOADS</h5><div class="num">1118</div></div>
  <div class="stat" style="left:899px"><div class="ring"><span><svg width="36" height="38" viewBox="0 0 36 38" fill="#fff"><circle cx="28" cy="7" r="6"/><circle cx="8" cy="19" r="6"/><circle cx="28" cy="31" r="6"/><path d="M8 19 28 7M8 19l20 12" stroke="#fff" stroke-width="3"/></svg></span></div><h5>SHARES</h5><div class="num">12548</div></div>
</section>

<section class="section cta">
  <h2>WASTE NO MORE TIME</h2>
  <div class="btn-outline">LEARN MORE <svg width="14" height="12" viewBox="0 0 14 12"><path d="M0 6h11M7 1l5 5-5 5" fill="none" stroke="#fff" stroke-width="2.5"/></svg></div>
</section>

<footer class="section footer">
  <div class="col" style="left:99px;width:250px">
    <h6>LAST 30 POSTS</h6>
    <ul><li>Best Destinations for RV Trip</li><li>How to Find Camp Grounds When<br>You're Traveling</li><li>Where to Find Mattresses for Your RV</li><li>How to Get Internet in Your RV</li><li>How to Prepare for a Road Trip in an RV</li><li>What Costs Come with Buying</li></ul>
  </div>
  <div class="col" style="left:394px">
    <h6>ARCHIVES BY MONTH</h6>
    <ul><li>September 2015</li><li>July 2015</li><li>June 2015</li><li>May 2015</li><li>April 2015</li><li>March 2015</li><li>February 2015</li></ul>
  </div>
  <div class="col news" style="left:680px">
    <h6 style="margin-top:0;margin-bottom:22px">ARCHIVES BY SUBJECT</h6>
    <ul><li>Uncategorized</li></ul>
    <h6>SIGN TO NEWSLETTER</h6>
    <p>Join our confidential network and be the</p>
    <div class="email">email</div>
    <div class="subscribe">SUBSCRIBE</div>
  </div>
  <div class="col follow" style="left:999px">
    <h6>FOLLOW US</h6>
    <ul><li><i></i>Linkplaza</li><li><i></i>Chirper</li><li><i></i>Vidstream</li></ul>
  </div>
  <p class="copyright">© Copyright 2016 BrightKestrel IT Consultancy.All Rights Reserved</p>
</footer>

</body>
</html>
```